Letterhead Creation

I would like to create a letterhead incorporating my family crest attached. My current letterhead with my information is also attached. I would also like to add my Paralegal Rosalind Merriweather

```html
<!DOCTYPE html>
<html lang="en">
<head>
<meta charset="utf-8">
<title>Letterhead – Mark Ives Esq.</title>
<link rel="stylesheet" href="https://fonts.googleapis.com/css2?family=Arimo:wght@400;700&family=Tinos:wght@400;700&display=swap">
<style>
  :root {
    --backdrop: #808080;
    --paper: #ffffff;
    --brand-blue: #1f3d9b;
    --ink: #1a1a1a;
    --muted: #333333;
    --rule-grey: #c9c9c9;
    --crest-blue: #2446a6;
  }
  * { box-sizing: border-box; margin: 0; padding: 0; }
  html, body { width: 937px; height: 1200px; overflow: hidden; }
  body { background: var(--backdrop); position: relative; }

  .sheet {
    position: absolute; left: 157px; top: 118px;
    width: 622px; height: 931px;
    background: var(--paper);
    box-shadow: 0 2px 6px rgba(0,0,0,0.35);
  }
  .sheet > * { position: absolute; }

  .paralegal-name {
    left: 58px; top: 34px;
    font: 700 13.5px/1 "Arimo", Arial, sans-serif;
    color: var(--brand-blue); letter-spacing: 0.4px;
  }
  .contact-list {
    left: 58px; top: 60px; width: 176px;
    font: 400 12px/14.4px "Arimo", Arial, sans-serif;
    color: var(--ink); list-style: none; white-space: nowrap;
  }
  .contact-list .label { color: var(--brand-blue); font-weight: 700; }
  .contact-divider {
    left: 242px; top: 61px; width: 1px; height: 44px; background: #555;
  }
  .office-address {
    left: 257px; top: 62px; font-style: normal;
    font: 400 11px/14px "Arimo", Arial, sans-serif; color: var(--muted);
  }
  .office-address strong { font-weight: 700; color: var(--ink); }
  .header-rule {
    left: 0; top: 119px; width: 406px; height: 2px; background: var(--brand-blue);
  }
  .family-crest {
    left: 427px; top: 24px; width: 151px; height: 158px;
    background: linear-gradient(180deg, #b8bfd6 0%, var(--crest-blue) 55%, #1a2f78 100%);
    border-radius: 20px 20px 75px 75px;
  }
  .crest-backdrop {
    left: 83px; top: 278px; width: 456px; height: 468px;
    background: radial-gradient(ellipse at center, #ededed 0%, #f5f5f5 55%, rgba(255,255,255,0) 75%);
  }

  .letter {
    left: 48px; top: 0; width: 528px;
    font: 400 13.2px/15.6px "Tinos", "Times New Roman", serif;
    color: var(--ink);
  }
  .letter > * { position: absolute; left: 0; width: 528px; }
  .issue-date { top: 180px; }
  .recipient { top: 240px; }
  .subject { top: 331px; font-weight: 700; }
  .salutation { top: 392px; }
  .body-one { top: 420px; text-align: justify; }
  .body-two { top: 486px; text-align: justify; }
  .body-three { top: 542px; }
  .closing { top: 602px; }
  sup { font-size: 8px; line-height: 0; }

  .footer-rule {
    left: 44px; top: 877px; width: 533px; height: 1px; background: var(--rule-grey);
  }
  .website {
    left: 0; width: 622px; top: 889px; text-align: center;
    font: 400 11px/1 "Arimo", Arial, sans-serif; color: var(--ink);
  }
</style>
</head>
<body>
  <main class="sheet">
    <div class="crest-backdrop" role="img" aria-label="Faint family crest watermark"></div>

    <h1 class="paralegal-name">PARALEGAL ROSALIND MERRIWEATHER</h1>
    <ul class="contact-list">
      <li><span class="label">Tel:</span> (555) 210-4471</li>
      <li><span class="label">Fax:</span> (555) 210-4480</li>
      <li><span class="label">Email:</span> Mark@Iveslawapc.com</li>
    </ul>
    <div class="contact-divider"></div>
    <address class="office-address">
      <strong>Mark Ives Esq.</strong><br>
      412 N. Alder Ave.<br>
      Linwood, Ca 91890
    </address>
    <div class="header-rule"></div>
    <div class="family-crest" role="img" aria-label="Family crest with helmet, mantling and shield"></div>

    <article class="letter">
      <p class="issue-date">Issuing date: May 5, 2012</p>
      <p class="recipient">Name of employee: Mr. xyz<br>Address of employee<br>address line 2</p>
      <p class="subject">Ref: Promotion as an Assistant secretary</p>
      <p class="salutation">Dear Mr. xyz,</p>
      <p class="body-one">I have the pleasure to inform you that you have been promoted as assistant secretary in the share department of the company. You are required to take charge of the new assignment on 15<sup>th</sup> May, 2012. Please accept my hearty congratulations on your promotion.</p>
      <p class="body-two">Your salary scale in the promoted cadre will be Tk. 16,000 and from 15th may, your basic salary will be fixed at Tk. 12,000 in the said scale. You will be entitled to all other allowances as applicable to the staff-ll of the company. Other services conditions remain unchanged.</p>
      <p class="body-three">Please acknowledge receipt of this letter.</p>
      <p class="closing">Yours sincerely,</p>
    </article>

    <div class="footer-rule"></div>
    <p class="website">www.iveslawapc.com</p>
  </main>
</body>
</html>
```